New website for out outstanding veterinary training center

We already have a beautiful logo with nice colors and we are now looking for a breathtaking modern website to present our training center and future corses held there. A section to book open courses should also be available.

We are planing the realize the website with Wordpress.
The following pages should be available:
- Startpage / Overview
- Page to present the different rooms and seating option
- Page where the rooms can be booked
- Page where recommended accommodation are presented
- Page to present and book corses
- contact page
- Impressum

Target Market(s)

European Union

Industry/Entity Type

Education, Veterinary medicine

Number of Pages Required

5+ page

Font styles to use
Sans Serif

Colors
00AB8E
00BBA5
67D7C9
C6EFE9
E9F9F6

Requirements
Must have
• The website must be clear and easy to read. The colors form the logos should be used for the design.
Should not have
• To playful design. The page is not for a veterinary practice. we are a training center for veterinarians!

```html
<!DOCTYPE html>
<html lang="en">
<head>
<meta charset="utf-8">
<title>Vetlanta Training Center</title>
<link href="https://fonts.googleapis.com/css2?family=Montserrat:ital,wght@0,400;0,500;0,600;0,700;1,400&display=swap" rel="stylesheet">
<style>
:root{
  --teal:#1b9389;
  --teal-dark:#147a71;
  --plum:#5b4852;
  --plum-text:#574650;
  --grey-bg:#f6f6f6;
  --text:#666;
  --line:#cfcfcf;
  --white:#fff;
}
*{margin:0;padding:0;box-sizing:border-box}
html,body{width:1200px;height:4751px;overflow:hidden}
body{position:relative;font-family:'Montserrat',sans-serif;color:var(--text);background:var(--white)}
.abs{position:absolute}
.btn{position:absolute;display:flex;align-items:center;justify-content:center;border-radius:30px;font-weight:600;font-size:17px;text-transform:uppercase;letter-spacing:.2px}
.btn-teal{background:var(--teal);color:var(--white)}
.section-title{position:absolute;left:0;width:1200px;text-align:center;font-weight:600;font-size:38px;color:var(--plum-text)}

/* header */
.site-header{position:absolute;left:0;top:0;width:1200px;height:120px;background:var(--white);z-index:3}
.header-contact{position:absolute;right:111px;top:24px;font-size:18px;font-weight:500;color:var(--plum-text);display:flex;align-items:center;gap:10px}
.header-contact svg{width:16px;height:16px;fill:var(--teal)}
.main-nav{position:absolute;right:111px;top:80px;display:flex;gap:25px;font-size:16px;font-weight:600;color:var(--plum-text)}
.main-nav .active{color:var(--teal)}
.logo-badge{position:absolute;left:80px;top:-40px;width:260px;height:258px;border-radius:50%;background:var(--white);z-index:4;display:flex;flex-direction:column;align-items:center;justify-content:flex-end;padding-bottom:40px}
.logo-mark{width:66px;height:66px;border-radius:50%;background:var(--teal);margin-bottom:10px}
.logo-name{font-weight:700;font-size:28px;color:var(--plum-text);line-height:1}
.logo-sub{font-weight:700;font-size:13px;color:var(--plum-text);letter-spacing:3px;margin-top:4px}

/* hero */
.hero{position:absolute;left:0;top:120px;width:1200px;height:690px;background:linear-gradient(100deg,#2f8f7f 0%,#c69a6a 40%,#e0b27a 60%,#2c9c8e 85%,#1d7f76 100%)}
.hero-title{position:absolute;left:111px;top:270px;font-weight:700;font-size:53px;line-height:66px;color:var(--white);text-transform:uppercase;z-index:2}
.hero-btn{left:111px;top:509px;width:236px;height:66px;background:var(--white);color:#333;font-size:18px}
.dots{position:absolute;display:flex;gap:4px}
.dots span{width:15px;height:15px;border-radius:50%;border:2px solid var(--white)}
.dots span.on{background:var(--white)}

/* welcome */
.welcome h2{position:absolute;left:111px;top:876px;font-weight:600;font-size:39px;line-height:47px;color:var(--plum-text)}
.welcome p{position:absolute;left:111px;width:470px;font-size:16px;line-height:30px;color:var(--text)}
.welcome-photo{position:absolute;left:612px;top:830px;width:490px;height:490px;border-radius:50%;border:12px solid var(--teal);background:radial-gradient(circle at 45% 50%,#8a6040 0%,#c9b49a 40%,#fff 75%)}

/* courses */
.courses{position:absolute;left:0;top:1386px;width:1200px;height:1244px;background:var(--grey-bg)}
.course-card{position:absolute;width:313px;height:476px;background:var(--white);box-shadow:0 2px 6px rgba(0,0,0,.12)}
.course-card .photo{height:240px}
.course-card h3{margin-top:26px;text-align:center;font-weight:600;font-size:23px;color:var(--plum-text)}
.course-card p{margin:14px auto 0;width:280px;text-align:center;font-size:15px;line-height:26px}
.course-card .btn{left:85px;top:408px;width:143px;height:46px}
.view-more{position:absolute;left:0;top:2545px;width:1200px;text-align:center;font-size:17px;font-weight:600;color:var(--teal)}

/* testimonials */
.testimonials{position:absolute;left:0;top:2632px;width:1200px;height:443px;background:linear-gradient(90deg,#2a9a8f,#3aa69a 50%,#2e9a8f)}
.testimonials .section-title{color:var(--white);top:46px}
.avatar{position:absolute;left:155px;top:159px;width:150px;height:150px;border-radius:50%;background:var(--plum)}
.quote{position:absolute;left:347px;top:168px;width:730px;font-style:italic;font-size:17px;line-height:30px;color:var(--white)}
.quote-name{position:absolute;left:347px;top:310px;font-weight:600;font-size:21px;color:var(--white)}

/* accommodations */
.acc-card{position:absolute;top:3218px;width:234px;height:293px}
.acc-card span{position:absolute;left:0;bottom:22px;width:100%;text-align:center;font-weight:600;font-size:22px;line-height:26px;color:var(--white)}
.arrow{position:absolute;top:3350px;width:20px;height:30px;stroke:var(--plum-text);stroke-width:3;fill:none}

/* contact */
.field{position:absolute;left:111px;width:508px;height:46px;border:1px solid var(--line);padding:11px 14px;font-size:16px;color:#888;background:var(--white)}
.contact-photo{position:absolute;left:665px;top:3747px;width:413px;height:387px;background:linear-gradient(135deg,#e9eef2 0%,#b07a52 50%,#2b6f9a 100%)}

/* footer */
.footer{position:absolute;left:0;top:4150px;width:1200px;height:601px}
.footer-logo{position:absolute;left:111px;top:181px;width:300px;display:flex;flex-direction:column;align-items:center}
.footer-logo .mark{width:190px;height:190px;border-radius:50%;border:8px solid var(--white);margin-bottom:20px}
.footer-logo .name{font-weight:700;font-size:50px;color:var(--white);line-height:1}
.footer-logo .sub{font-weight:700;font-size:24px;letter-spacing:6px;color:var(--white);margin-top:6px}
.footer h4{position:absolute;top:214px;font-weight:600;font-size:16px;color:var(--white);text-transform:uppercase}
.quick-links{position:absolute;left:514px;top:254px;list-style:none;font-size:15px;line-height:27.6px;color:var(--white)}
.contact-info{position:absolute;left:761px;font-size:15px;line-height:30px;color:var(--white);display:flex;gap:10px}
.contact-info svg{width:14px;height:14px;fill:var(--teal);margin-top:8px;flex-shrink:0}
.footer-rule{position:absolute;left:111px;top:495px;width:978px;height:1px;background:rgba(255,255,255,.25)}
.copyright{position:absolute;left:111px;top:530px;font-size:15px;color:var(--white)}
.social{position:absolute;top:519px;width:40px;height:40px;border-radius:50%;border:1.5px solid var(--white)}
</style>
</head>
<body>

<header class="site-header">
  <div class="header-contact">
    <svg viewBox="0 0 24 24"><path d="M6.6 10.8a15 15 0 006.6 6.6l2.2-2.2a1 1 0 011-.25 11.4 11.4 0 003.6.57 1 1 0 011 1V20a1 1 0 01-1 1A17 17 0 013 4a1 1 0 011-1h3.5a1 1 0 011 1 11.4 11.4 0 00.57 3.6 1 1 0 01-.25 1z"/></svg>
    <span>1 800 555 0142</span><span>|</span>
    <svg viewBox="0 0 24 24"><path d="M2 5h20v14H2z M2 5l10 8 10-8" /></svg>
    <span>info@vetlantatraining.example</span>
  </div>
  <nav class="main-nav">
    <span class="active">HOME</span><span>ABOUT US</span><span>COURSES</span><span>ACCOMODATION</span><span>CONTACT US</span>
  </nav>
</header>
<div class="logo-badge">
  <div class="logo-mark"></div>
  <div class="logo-name">Vetlanta</div>
  <div class="logo-sub">TRAINING CENTER</div>
</div>

<section class="hero" role="img" aria-label="Smiling veterinarian in teal scrubs holding a pug dog"></section>
<h1 class="hero-title">Outstanding<br>Veterinary<br>Training Center</h1>
<div class="btn hero-btn">Book a Workshop</div>
<div class="dots" style="left:572px;top:696px"><span class="on"></span><span></span><span></span></div>
<svg class="abs" style="left:0;top:700px;z-index:1" width="1200" height="120" viewBox="0 0 1200 120">
  <path d="M0 20 Q300 0 600 110 Q900 0 1200 20 V120 H0Z" fill="#fff"/>
  <path d="M0 20 Q300 0 600 110 Q900 0 1200 20" fill="none" stroke="#5b4852" stroke-width="5"/>
</svg>

<section class="welcome">
  <h2>Welcome to Vetlanta<br>Training Center</h2>
  <p style="top:992px">Lorem ipsum dolor sit amet, consectetur adipiscing elise do eiusmod tempor incididunt ut.</p>
  <p style="top:1081px">Nioostrud exercitation ullamco laboris nisi ut aliquip ealo mmodo consequat. Duis aute irure dolor in repreherit in voluptate velit esse cillum dolore eu fugiat nulla pariatur teur sint occaecat cupidatat sunt.</p>
  <div class="btn btn-teal" style="left:111px;top:1231px;width:154px;height:50px">Read More</div>
  <div class="welcome-photo" role="img" aria-label="Tricolour dog sitting beside a tabby cat"></div>
</section>

<section class="courses">
  <h2 class="section-title" style="top:60px">Courses</h2>
</section>
<article class="course-card" style="left:111px;top:1524px"><div class="photo" role="img" aria-label="Vet checking a dog's teeth" style="background:linear-gradient(135deg,#1f8a7c,#d9b49a)"></div><h3>Dentistry for vets</h3><p>Nemo enim ipsam voluptatem quia voluptas sit aspernatur auod it aut fugi sed quia conse.</p><div class="btn btn-teal">Book Now</div></article>
<article class="course-card" style="left:443px;top:1524px"><div class="photo" role="img" aria-label="Sedated dog on an operating table" style="background:linear-gradient(135deg,#c8d3d8,#c88a4a 60%,#5fb9b3)"></div><h3>Anaesthesia</h3><p>Nemo enim ipsam voluptatem quia voluptas sit aspernatur auod it aut fugi sed quia conse.</p><div class="btn btn-teal">Book Now</div></article>
<article class="course-card" style="left:775px;top:1524px"><div class="photo" role="img" aria-label="Vet examining a cat's eyes" style="background:linear-gradient(135deg,#3a3a3a,#8a8780 50%,#2a4f8a)"></div><h3>Ophthalmology</h3><p>Nemo enim ipsam voluptatem quia voluptas sit aspernatur auod it aut fugi sed quia conse.</p><div class="btn btn-teal">Book Now</div></article>
<article class="course-card" style="left:111px;top:2022px"><div class="photo" role="img" aria-label="Dachshund with a mobility wheelchair" style="background:linear-gradient(135deg,#e6d2bf,#9a6a45 55%,#c9b29a)"></div><h3>Orthopaedic</h3><p>Nemo enim ipsam voluptatem quia voluptas sit aspernatur auod it aut fugi sed quia conse.</p><div class="btn btn-teal">Book Now</div></article>
<article class="course-card" style="left:443px;top:2022px"><div class="photo" role="img" aria-label="Dog and cat playing on grass" style="background:linear-gradient(160deg,#e9c48a,#b58a5e 50%,#4f9a3a)"></div><h3>Behaviour</h3><p>Nemo enim ipsam voluptatem quia voluptas sit aspernatur auod it aut fugi sed quia conse.</p><div class="btn btn-teal">Book Now</div></article>
<article class="course-card" style="left:775px;top:2022px"><div class="photo" role="img" aria-label="Vet bandaging a dog's leg" style="background:linear-gradient(135deg,#6e5a4a,#e8e4df 55%,#4a78a8)"></div><h3>Emergency Care</h3><p>Nemo enim ipsam voluptatem quia voluptas sit aspernatur auod it aut fugi sed quia conse.</p><div class="btn btn-teal">Book Now</div></article>
<div class="view-more">VIEW MORE</div>

<section class="testimonials">
  <h2 class="section-title">Testimonials</h2>
  <div class="avatar" role="img" aria-label="Client profile placeholder">
    <svg width="150" height="150" viewBox="0 0 150 150"><circle cx="75" cy="58" r="28" fill="#fff"/><path d="M28 128 Q75 70 122 128 Q75 150 28 128Z" fill="#fff"/></svg>
  </div>
  <p class="quote">“ At vero eos et accusamus et iusto odio dignissimosers ducimus qui blanditiis ntium voluptatum deleniti atque corrupti quos dolores et quas molestias excep turi sint occae cati cupiditate non provident, similique sunt in culpa qui officiad mollitia animi, id est laborum et dolorum facilis est “</p>
  <div class="quote-name">John Doe</div>
  <div class="dots" style="left:572px;top:352px"><span class="on"></span><span></span><span></span></div>
</section>

<h2 class="section-title" style="top:3136px">Our Accommodations</h2>
<svg class="arrow" style="left:58px" viewBox="0 0 20 30"><path d="M16 2L4 15l12 13"/></svg>
<div class="acc-card" role="img" aria-label="Seminar room with rows of desks" style="left:111px;background:linear-gradient(180deg,#eef0f2,#b9b2a8 55%,#2a2f4a)"><span>Seminar<br>Room</span></div>
<div class="acc-card" role="img" aria-label="Veterinary lab training room" style="left:359px;background:linear-gradient(180deg,#d8dde0,#9aa3a8 55%,#4a5458)"><span>Vet Lab<br>Training Room</span></div>
<div class="acc-card" role="img" aria-label="Board and meeting room" style="left:608px;background:linear-gradient(180deg,#f2f2f2,#c8c8c8 55%,#3a3a3a)"><span>Board and<br>Meeting Rooms</span></div>
<div class="acc-card" role="img" aria-label="Kitchen facilities" style="left:855px;background:linear-gradient(180deg,#e8e2da,#b4aaa0 55%,#5a524a)"><span>Kitchen<br>Facilities</span></div>
<svg class="arrow" style="left:1122px" viewBox="0 0 20 30"><path d="M4 2l12 13L4 28"/></svg>

<h2 class="section-title" style="top:3657px">Contact Us</h2>
<div class="field" style="top:3747px">Name*</div>
<div class="field" style="top:3810px">Email*</div>
<div class="field" style="top:3871px">Subject*</div>
<div class="field" style="top:3933px;height:125px">Message</div>
<div class="btn btn-teal" style="left:111px;top:4086px;width:126px;height:50px">Submit</div>
<div class="contact-photo" role="img" aria-label="Veterinarian examining a husky dog"></div>

<footer class="footer">
  <svg class="abs" style="left:0;top:0" width="1200" height="601" viewBox="0 0 1200 601">
    <path d="M0 120 Q300 120 600 20 Q900 120 1200 120 V601 H0Z" fill="#5b4852"/>
    <path d="M0 110 Q300 110 600 10 Q900 110 1200 110" fill="none" stroke="#5b4852" stroke-width="4"/>
  </svg>
  <div class="footer-logo">
    <div class="mark"></div>
    <div class="name">Vetlanta</div>
    <div class="sub">TRAINING CENTER</div>
  </div>
  <h4 style="left:514px">Quick Links</h4>
  <ul class="quick-links">
    <li>Home</li><li>About us</li><li>Courses</li><li>Accomodation</li><li>Contact us</li><li>Privacy statement</li><li>Terms &amp; conditions</li>
  </ul>
  <h4 style="left:761px">Contact Information</h4>
  <div class="contact-info" style="top:250px"><svg viewBox="0 0 24 24"><path d="M12 2a7 7 0 00-7 7c0 5 7 13 7 13s7-8 7-13a7 7 0 00-7-7zm0 9.5A2.5 2.5 0 1112 6a2.5 2.5 0 010 5.5z"/></svg><span>Lindenweg 12 - 14<br>D-80331 Musterstadt</span></div>
  <div class="contact-info" style="top:343px"><svg viewBox="0 0 24 24"><path d="M6.6 10.8a15 15 0 006.6 6.6l2.2-2.2a1 1 0 011-.25 11.4 11.4 0 003.6.57 1 1 0 011 1V20a1 1 0 01-1 1A17 17 0 013 4a1 1 0 011-1h3.5a1 1 0 011 1 11.4 11.4 0 00.57 3.6 1 1 0 01-.25 1z"/></svg><span>1 800 555 0142</span></div>
  <div class="contact-info" style="top:407px"><svg viewBox="0 0 24 24"><path d="M2 4h20v16H2z" /></svg><span>info@vetlantatraining.example</span></div>
  <div class="footer-rule"></div>
  <div class="copyright">© 2021 Vetlanta Training Center. All Rights Reserved.</div>
  <div class="social" style="left:944px"></div>
  <div class="social" style="left:994px"></div>
  <div class="social" style="left:1043px"></div>
</footer>

</body>
</html>
```